Flyer design for company which solely specializes in transferring Videos to DVD

I would like a flyer designed for my small business i own a digital transferring business which solely specializes in transferring videos to DVD.

My company is called tapeshiftdisc.

This flyer will be going through peoples doors and will be my first impression of the company. It needs to make them call me and transfer their videos.

In the must have section i have included a few lines of text i would like to include, please take any other information you think is necessary from my website and include it.

The flyer will be size A5 and double sided!

Target Market(s)

age group 30+ who want their home movies transferred on to DVD

Industry/Entity Type

Small Business

Requirements
Must have
• The flyer must include:

Company Logo - attached image

Headline of - Take action don't lose your precious home movies!

Did you know the average video tape has a shelf life of between 15-20 years, after this time period the quality starts to degrade.

Here at Tapeshiftdisc we offer a specialist service in transferring videos to DVD.

We pride ourselves on being the cheapest and best service in the whole of the UK.

There are no expensive postage fees as we hand collect and deliver your videos free of charge!

Prices:
Transfer for first copy = £7
Additional copies = £3

Order before July 31st and receive 10% off.

Order now either by telephone on 07861203574 or email tapeshiftdisc@postbrook.co.uk.

For more information go to our website address www.tapeshiftdisc.co.uk

Testimonials

"Your service was brilliant the DVD’s were of the highest quality and the lowest price I have come across, I will be recommending you to all my friends!"

Colin from Midsomer Norton

"Just wanted to say thanks for an amazing service, it was super fast and it’s brilliant to see the old family movies which we haven’t seen for years!!!"

Wendy from Midsomer Norton
Nice to have
• I would like the color scheme to be orange black and white as this is the colors of my website. However i am happy to try different colors and i am very open minded.

The website is currently under.
www.tapeshiftdisc.co.uk

```html
<!DOCTYPE html>
<html lang="en">
<head>
<meta charset="utf-8">
<title>Tapeshiftdisc – A5 Flyer, Front and Back</title>
<link rel="stylesheet" href="https://fonts.googleapis.com/css2?family=Michroma&family=Orbitron:wght@700;900&family=Questrial&display=swap">
<style>
  :root {
    --stage: #2a2a2c;
    --flyer-black: #060606;
    --ink-white: #ffffff;
    --ink-yellow: #e6d53a;
    --ink-yellow-deep: #b9a71c;
    --disc-green: #3d4415;
    --vcr-green: #4fbf2a;
    --header-white: #f6f6f6;
  }
  * { box-sizing: border-box; margin: 0; padding: 0; }
  html, body { width: 1200px; height: 800px; overflow: hidden; }
  body {
    background: var(--stage);
    font-family: "Questrial", sans-serif;
    position: relative;
  }
  .flyer {
    position: absolute;
    top: 50px;
    width: 495px;
    height: 700px;
    background: var(--flyer-black);
    overflow: hidden;
    color: var(--ink-white);
  }
  .flyer--front { left: 75px; }
  .flyer--back { left: 630px; }

  /* Artwork placeholders */
  .artwork {
    position: absolute;
    border-radius: 6px;
  }
  .artwork--front {
    left: 0; top: 300px; width: 495px; height: 350px;
    background:
      radial-gradient(ellipse at 35% 30%, rgba(110,120,30,.65), transparent 55%),
      radial-gradient(ellipse at 40% 90%, rgba(79,191,42,.35), transparent 60%),
      linear-gradient(180deg, #0b0d05, #10160a);
  }
  .artwork--back {
    left: 0; top: 300px; width: 495px; height: 330px;
    background:
      radial-gradient(ellipse at 30% 25%, rgba(80,90,25,.7), transparent 55%),
      radial-gradient(ellipse at 75% 75%, rgba(79,191,42,.35), transparent 55%),
      linear-gradient(180deg, #0a0b05, #0f1509);
  }

  /* Front */
  .brand-band {
    position: absolute; left: 0; top: 0; width: 100%; height: 68px;
    background: var(--header-white);
    display: flex; align-items: center; gap: 16px; padding-left: 26px;
  }
  .brand-band__mark { width: 30px; height: 30px; background: var(--flyer-black); }
  .brand-band__name {
    font-family: "Michroma", sans-serif;
    font-size: 30px; color: var(--flyer-black); letter-spacing: 1px;
  }
  .headline {
    position: absolute; left: 24px; top: 84px; width: 450px;
    font-family: "Michroma", sans-serif;
    font-size: 20px; line-height: 1.25; color: var(--ink-yellow);
    text-transform: uppercase;
  }
  .intro {
    position: absolute; left: 24px; top: 160px; width: 450px;
    font-size: 18px; line-height: 1.45; color: var(--ink-yellow);
    text-align: center;
  }
  .price {
    position: absolute; color: var(--ink-yellow);
    display: flex; align-items: flex-end; gap: 10px;
  }
  .price__label { font-size: 17px; line-height: 1.15; text-align: center; }
  .price__amount {
    font-family: "Orbitron", sans-serif; font-weight: 900;
    font-size: 52px; line-height: 1;
    background: linear-gradient(180deg, #f3ea7a, var(--ink-yellow-deep));
    -webkit-background-clip: text; background-clip: text; color: transparent;
  }
  .price__amount small { font-size: 26px; }
  .price--extra { right: 24px; top: 250px; }
  .price--first { left: 40px; top: 320px; }
  .price--first .price__amount { font-size: 64px; }
  .pitch {
    position: absolute; right: 22px; top: 410px; width: 250px;
    font-size: 14px; line-height: 1.4; text-align: center;
  }
  .pitch p + p { margin-top: 10px; }
  .offer-strip {
    position: absolute; left: 0; bottom: 24px; width: 100%;
    text-align: center; font-size: 15px; letter-spacing: 1px;
    text-transform: uppercase;
  }
  .offer-strip strong { font-size: 22px; font-weight: normal; }

  /* Back */
  .order-badge {
    position: absolute; left: 28px; top: 32px; width: 110px; height: 110px;
    border-radius: 50%;
    background: radial-gradient(circle at 40% 35%, #efe160, var(--ink-yellow-deep));
    display: flex; align-items: center; justify-content: center;
    text-align: center; font-size: 20px; line-height: 1.1;
    color: var(--ink-white); text-transform: uppercase; font-weight: bold;
  }
  .contact {
    position: absolute; left: 150px; top: 30px; width: 320px;
    text-align: center; text-transform: uppercase; line-height: 1.2;
  }
  .contact__lead { font-size: 15px; }
  .contact__phone { font-size: 30px; letter-spacing: 1px; }
  .contact__or { font-size: 12px; }
  .contact__email { font-size: 14px; }
  .testimonials {
    position: absolute; left: 36px; top: 170px; width: 423px;
    text-align: center; font-size: 13.5px; line-height: 1.4;
  }
  .testimonials__title { font-size: 19px; margin-bottom: 14px; }
  .testimonial__author { margin: 12px 0 16px; }
  .web-strip {
    position: absolute; left: 0; bottom: 22px; width: 100%;
    text-align: center; font-size: 15px; line-height: 1.45;
    letter-spacing: .5px; text-transform: uppercase;
  }
</style>
</head>
<body>

<section class="flyer flyer--front" aria-label="Flyer front">
  <div class="artwork artwork--front" role="img" aria-label="Photo of a VHS cassette over a glowing DVD disc with a green VCR clock display"></div>

  <header class="brand-band">
    <span class="brand-band__mark"></span>
    <span class="brand-band__name">TAPESHIFTDISC</span>
  </header>

  <h1 class="headline">Take action don't lose your precious home movies!</h1>

  <p class="intro">Did you know the average video tape has a shelf life of between 15-20 years, after this time period the quality starts to degrade.</p>

  <div class="price price--extra">
    <span class="price__label">Additional<br>copies</span>
    <span class="price__amount">£3<small>.00</small></span>
  </div>

  <div class="price price--first">
    <span class="price__label">Transfer for<br>first copy</span>
    <span class="price__amount">£7<small>.00</small></span>
  </div>

  <div class="pitch">
    <p>Here at Tapeshiftdisc we offer a specialist service in transferring videos to DVD.</p>
    <p>We pride ourselves on being the cheapest and best service in the whole of the UK.</p>
    <p>There are no expensive postage fees as we hand collect and deliver your videos free of charge!</p>
  </div>

  <p class="offer-strip">Order before July 31st and receive <strong>10% off</strong></p>
</section>

<section class="flyer flyer--back" aria-label="Flyer back">
  <div class="artwork artwork--back" role="img" aria-label="Photo of a VHS cassette on a DVD-R disc with a green VCR clock display"></div>

  <div class="order-badge">Order<br>now</div>

  <div class="contact">
    <p class="contact__lead">Either by telephone on</p>
    <p class="contact__phone">07861203574</p>
    <p class="contact__or">or email</p>
    <p class="contact__email">tapeshiftdisc@postbrook.co.uk</p>
  </div>

  <div class="testimonials">
    <h2 class="testimonials__title">Testimonials</h2>
    <blockquote class="testimonial">“Your service was brilliant the DVD's were of the highest quality and the lowest price I have come across, I will be recommending you to all my friends!”</blockquote>
    <p class="testimonial__author">Colin from Midsomer Norton</p>
    <blockquote class="testimonial">“Just wanted to say thanks for an amazing service, it was super fast and it's brilliant to see the old family movies which we haven't seen for years!!!”</blockquote>
    <p class="testimonial__author">Wendy from Midsomer Norton</p>
  </div>

  <p class="web-strip">For more information go to our website<br>address www.tapeshiftdisc.co.uk</p>
</section>

</body>
</html>
```